Smart Coffee Shop Needs a Poster Design

New smart coffee shop called Brewlo using touch screens as table tops. all information in attached file. the café is now open in a busy mall in Abu Dhabi.
We need creative design for 2 posters on two sides of a column. This is to attract the attention of people from a distance. We need it to be colorful and preferably in two languages: English and Arabic.
The dimensions are: 275 (H) x 75 (W) cm & 275 (H) x 87 (W) cm.
Catch phrase could be: The Smartest and Coolest Café on Earth. or something similar. Attached also is the hoarding poster.
Updates
Project Deadline Extended
Reason: Received 8 designs only. Still looking for more creative ideas. If we select your design, we will be providing more jobs (website, facebook, brochures, flyers, more posters etc..).
Industry/Entity Type
Coffee Shop
Look and feel
Each slider illustrates characteristics of the customer's brand and the style your logo design should communicate.

```html
<!DOCTYPE html>
<html lang="en">
<head>
<meta charset="utf-8">
<title>Brewlo – Smart Coffee Shop Column Posters</title>
<link rel="stylesheet" href="https://fonts.googleapis.com/css2?family=PT+Sans:wght@400;700&display=swap">
<style>
  :root {
    --purple: #66318f;
    --yellow: #ece61f;
    --white: #ffffff;
    --brown: #8a4b22;
    --ink: #111111;
    --page: #ffffff;
  }
  html, body {
    margin: 0;
    padding: 0;
    width: 1000px;
    height: 1200px;
    overflow: hidden;
    background: var(--page);
    font-family: "PT Sans", "Myriad Pro", Arial, sans-serif;
  }
  .board {
    position: relative;
    width: 1000px;
    height: 1200px;
  }
  .option-label {
    position: absolute;
    top: 575px;
    margin: 0;
    font-size: 44px;
    font-weight: 400;
    color: var(--ink);
    white-space: nowrap;
    transform: translate(-50%, -50%) rotate(-90deg);
  }
  .option-label--one { left: 75px; }
  .option-label--two { left: 546px; }
  .poster {
    position: absolute;
    top: 18px;
    width: 318px;
    height: 1167px;
    box-shadow: 2px 3px 8px rgba(0, 0, 0, 0.25);
    background: var(--white);
  }
  .poster--one { left: 137px; }
  .poster--two { left: 603px; }
  .poster svg { display: block; }
  .fill-purple { fill: var(--purple); }
  .fill-white { fill: var(--white); }
  .headline-small, .headline-sub { fill: var(--white); font-weight: 400; }
  .headline-main { fill: var(--yellow); font-weight: 700; }
  .tagline-top { fill: var(--yellow); font-size: 15.5px; font-weight: 700; }
  .tagline-bottom { fill: var(--brown); font-size: 16px; font-weight: 400; }
  .brand-name { fill: var(--yellow); font-size: 62px; font-weight: 700; }
</style>
</head>
<body>
<main class="board">

  <p class="option-label option-label--one">Option 01</p>

  <section class="poster poster--one" aria-label="Poster option 01">
    <svg width="318" height="1167" viewBox="0 0 318 1167" xmlns="http://www.w3.org/2000/svg">
      <defs>
        <linearGradient id="photo-one-tones" x1="0" y1="0" x2="1" y2="1">
          <stop offset="0" stop-color="#eae6e2"/>
          <stop offset="0.35" stop-color="#d7b59b"/>
          <stop offset="0.6" stop-color="#4a73b8"/>
          <stop offset="1" stop-color="#35558e"/>
        </linearGradient>
        <linearGradient id="mug-one-tones" x1="0" y1="0" x2="1" y2="0">
          <stop offset="0" stop-color="#d9d9d9"/>
          <stop offset="0.5" stop-color="#ffffff"/>
          <stop offset="1" stop-color="#cfcfcf"/>
        </linearGradient>
        <path id="arc-top-one" d="M6 852 Q159 764 312 852"/>
        <path id="arc-bottom-one" d="M6 910 Q159 826 312 910"/>
      </defs>

      <rect class="photo" x="0" y="290" width="318" height="540" fill="url(#photo-one-tones)"
            role="img" aria-label="Photo of a smiling couple sitting together looking at a smartphone"/>

      <path class="header-band fill-purple" d="M0 0 H318 V178 C280 255 38 255 0 178 Z"/>
      <text class="headline-small" x="300" y="60" font-size="34" text-anchor="end">World’s # First</text>
      <text class="headline-main" x="158" y="126" font-size="88" text-anchor="middle">Smart</text>
      <text class="headline-sub" x="158" y="172" font-size="46" text-anchor="middle">Coffee Shop</text>

      <rect class="mug" x="114" y="190" width="106" height="100" rx="8" fill="url(#mug-one-tones)"
            role="img" aria-label="Photo of a white branded coffee mug"/>

      <path class="footer-band fill-purple" d="M0 812 Q159 738 318 812 V1167 H0 Z"/>
      <path class="footer-stripe fill-white" d="M0 866 Q159 782 318 866 L318 925 Q159 840 0 925 Z"/>
      <ellipse class="brand-disc fill-white" cx="159" cy="1140" rx="180" ry="200"/>

      <text class="tagline-top"><textPath href="#arc-top-one" startOffset="50%" text-anchor="middle">It’s not just about serving the food &amp; drinks,</textPath></text>
      <text class="tagline-bottom"><textPath href="#arc-bottom-one" startOffset="50%" text-anchor="middle">It is also about creating an atmosphere</textPath></text>

      <text class="brand-name" x="159" y="1105" text-anchor="middle">Brewlo</text>
    </svg>
  </section>

  <p class="option-label option-label--two">Option 02</p>

  <section class="poster poster--two" aria-label="Poster option 02">
    <svg width="318" height="1167" viewBox="0 0 318 1167" xmlns="http://www.w3.org/2000/svg">
      <defs>
        <linearGradient id="photo-two-tones" x1="0" y1="0" x2="1" y2="1">
          <stop offset="0" stop-color="#8a5a3c"/>
          <stop offset="0.35" stop-color="#e2c2ab"/>
          <stop offset="0.65" stop-color="#a9c6e2"/>
          <stop offset="1" stop-color="#4b4f56"/>
        </linearGradient>
        <linearGradient id="mug-two-tones" x1="0" y1="0" x2="1" y2="0">
          <stop offset="0" stop-color="#d9d9d9"/>
          <stop offset="0.5" stop-color="#ffffff"/>
          <stop offset="1" stop-color="#cfcfcf"/>
        </linearGradient>
        <path id="arc-top-two" d="M6 852 Q159 764 312 852"/>
        <path id="arc-bottom-two" d="M6 910 Q159 826 312 910"/>
      </defs>

      <rect class="photo" x="0" y="200" width="318" height="630" fill="url(#photo-two-tones)"
            role="img" aria-label="Photo of a smiling woman and man leaning over a touch-screen table"/>
      <path class="photo-edge fill-white" d="M0 0 H318 V262 Q159 220 0 290 Z"/>

      <path class="header-band fill-purple" d="M0 0 H318 V178 C280 255 38 255 0 178 Z"/>
      <text class="headline-small" x="300" y="60" font-size="34" text-anchor="end">World’s # First</text>
      <text class="headline-main" x="158" y="126" font-size="88" text-anchor="middle">Smart</text>
      <text class="headline-sub" x="158" y="172" font-size="46" text-anchor="middle">Coffee Shop</text>

      <rect class="mug" x="114" y="190" width="106" height="100" rx="8" fill="url(#mug-two-tones)"
            role="img" aria-label="Photo of a white branded coffee mug"/>

      <path class="footer-band fill-purple" d="M0 812 Q159 738 318 812 V1167 H0 Z"/>
      <path class="footer-stripe fill-white" d="M0 866 Q159 782 318 866 L318 925 Q159 840 0 925 Z"/>
      <ellipse class="brand-disc fill-white" cx="159" cy="1140" rx="180" ry="200"/>

      <text class="tagline-top"><textPath href="#arc-top-two" startOffset="50%" text-anchor="middle">It’s not just about serving the food &amp; drinks,</textPath></text>
      <text class="tagline-bottom"><textPath href="#arc-bottom-two" startOffset="50%" text-anchor="middle">It is also about creating an atmosphere</textPath></text>

      <text class="brand-name" x="159" y="1105" text-anchor="middle">Brewlo</text>
    </svg>
  </section>

</main>
</body>
</html>
```